Plakat für Hersteller von Maultaschen und Knödeln
Zielgruppe
Mit meiner Manufaktur Rinnfalten & Co stelle ich Maultaschen und Knödel her. Produziert wird mit hochwertigen, möglichst regionalen Zutaten und mit dem Anspruch, traditionelle Klassiker in zeitgemäßer Qualität anzubieten.
Im Mittelpunkt stehen Frische, Transparenz und ehrliches Handwerk. Die Produkte werden mit Sorgfalt hergestellt und sind für den direkten Verkauf auf dem Brunnwaldener Wochenmarkt bestimmt. Rinnfalten & Co verbindet bodenständige Küche mit regionaler Identität – unkompliziert, authentisch und genussorientiert.
Zielgruppe rund um den Brunnwaldener Wochenmarkt:
- Marktbesucher mit Qualitätsbewusstsein, die gezielt regionale und handwerklich hergestellte Lebensmittel kaufen
- Berufstätige und Familien, die hochwertige, frisch produzierte Gerichte für zu Hause suchen
- Genussorientierte Kundinnen und Kunden, die traditionelle Küche schätzen
- Seniorinnen und Senioren, die klassische Hausmannskost bevorzugen
- Regionalverbundenen Verbraucherinnen und Verbrauchern, die lokale Anbieter unterstützen möchten
Der Brunnwaldener Wochenmarkt zieht ein vielfältiges Publikum an, das Wert auf persönliche Beratung, Frische und nachvollziehbare Herkunft legt. Rinnfalten positioniert sich hier als authentischer, spezialisierter Anbieter für handgemachte Teigklassiker mit klarem kulinarischem Profil.
Aufgabenstellung
Das Plakat soll in A5, A4, A3 und A2 nutzbar sein und der Text soll austauschbar sein.
Das Plakat soll gut zum Wochenmarkt passen und ehrliches, qualitativ hochwertiges Handwerk ausdrücken und vor allem Lust auf Maultaschen und Knödel machen. Es soll zu meinen Marktstand (Monza Rot) und dem Logo passen. Das Logo soll sehr präsent sein.

```html
<!DOCTYPE html>
<html lang="de">
<head>
<meta charset="utf-8">
<title>Rinnfalten &amp; Co – Plakat</title>
<link rel="stylesheet" href="https://fonts.googleapis.com/css2?family=Bebas+Neue&family=Lobster&family=Lato:wght@300;400;700&display=swap">
<style>
  :root {
    --monza: #a5131c;
    --cream: #f4e7b2;
    --white: #ffffff;
    --ink: #161616;
    --ink-soft: #444444;
    --parchment-light: #e6d3a4;
    --parchment-mid: #c9a56a;
    --logo-green: #8ab61d;
    --stage: #d4d4d4;
  }
  html, body {
    margin: 0;
    padding: 0;
    width: 800px;
    height: 1200px;
    overflow: hidden;
    background: var(--stage);
  }
  .poster {
    position: absolute;
    left: 0;
    top: 34px;
    width: 800px;
    height: 1131px;
    background: var(--monza);
    overflow: hidden;
    font-family: "Lato", sans-serif;
  }
  .logo-field {
    position: absolute;
    left: -150px;
    top: -330px;
    width: 520px;
    height: 540px;
    border-radius: 50%;
    background: var(--white);
  }
  .brand {
    position: absolute;
    left: 58px;
    top: 70px;
    display: flex;
    align-items: center;
    gap: 14px;
  }
  .brand-dot {
    width: 26px;
    height: 26px;
    border-radius: 50%;
    background: var(--logo-green);
  }
  .brand-name {
    font-family: "Lato", sans-serif;
    font-weight: 700;
    font-size: 30px;
    color: var(--monza);
    white-space: nowrap;
  }
  .headline {
    position: absolute;
    left: 46px;
    top: 250px;
    margin: 0;
    font-family: "Bebas Neue", sans-serif;
    font-weight: 400;
    font-size: 84px;
    line-height: 63px;
    letter-spacing: 3px;
    color: var(--cream);
  }
  .subline {
    position: absolute;
    left: 48px;
    top: 446px;
    margin: 0;
    font-family: "Lobster", cursive;
    font-size: 27px;
    color: var(--cream);
    white-space: nowrap;
  }
  .benefits {
    position: absolute;
    left: 42px;
    top: 580px;
    margin: 0;
    padding: 0;
    list-style: none;
  }
  .benefit {
    position: relative;
    padding-left: 34px;
    margin-bottom: 22px;
  }
  .benefit::before {
    content: "";
    position: absolute;
    left: 2px;
    top: 10px;
    width: 8px;
    height: 8px;
    border-radius: 50%;
    background: var(--cream);
    box-shadow: 0 0 0 3px var(--monza), 0 0 0 5px var(--cream);
  }
  .benefit-title {
    display: block;
    font-family: "Lobster", cursive;
    font-size: 25px;
    color: var(--cream);
    line-height: 30px;
    white-space: nowrap;
  }
  .benefit-text {
    display: block;
    margin-top: 6px;
    font-weight: 300;
    font-size: 19px;
    letter-spacing: 0.4px;
    color: var(--cream);
    white-space: nowrap;
  }
  .scroll-art {
    position: absolute;
    left: 499px;
    top: 37px;
    width: 301px;
    height: 896px;
    background: linear-gradient(90deg, var(--parchment-mid) 0%, var(--parchment-light) 40%, var(--parchment-light) 100%);
  }
  .food-photo {
    position: absolute;
    left: 569px;
    width: 223px;
    height: 200px;
  }
  .photo-dough { top: 179px; background: linear-gradient(160deg, #efeae2 0%, #d8c8a8 60%, #b89a6a 100%); }
  .photo-knoedel { top: 387px; background: radial-gradient(circle at 55% 45%, #e0a54a 0%, #b0702a 45%, #4a3020 100%); }
  .photo-maultasche { top: 595px; background: radial-gradient(circle at 50% 50%, #e8b860 0%, #a46a2c 50%, #3a2a20 100%); }
  .visit-band {
    position: absolute;
    left: 0;
    top: 969px;
    width: 800px;
    height: 162px;
    background: var(--white);
    text-align: center;
  }
  .visit-call {
    margin: 24px 0 0;
    font-weight: 700;
    font-size: 27.5px;
    line-height: 38px;
    color: var(--ink);
    white-space: nowrap;
  }
  .visit-tagline {
    margin: 6px 0 0;
    font-weight: 300;
    font-size: 20px;
    letter-spacing: 0.2px;
    color: var(--ink-soft);
    white-space: nowrap;
  }
</style>
</head>
<body>
  <main class="poster">
    <div class="logo-field"></div>
    <div class="brand">
      <span class="brand-dot"></span>
      <span class="brand-name">Rinnfalten &amp; Co</span>
    </div>

    <h1 class="headline">ECHT.<br>HANDGEMACHT.<br>LECKER.</h1>
    <p class="subline">Maultaschen &amp; Knödel wie hausgemacht.</p>

    <ul class="benefits">
      <li class="benefit">
        <span class="benefit-title">Frische aus der Region:</span>
        <span class="benefit-text">Hochwertige Zutaten, ehrliches Handwerk.</span>
      </li>
      <li class="benefit">
        <span class="benefit-title">Tradition trifft Moderne:</span>
        <span class="benefit-text">Klassische Rezepte in zeitgemäßer Qualität.</span>
      </li>
      <li class="benefit">
        <span class="benefit-title">Direkt vom Erzeuger:</span>
        <span class="benefit-text">Mit Liebe in unserer Manufaktur hergestellt.</span>
      </li>
    </ul>

    <div class="scroll-art" role="img" aria-label="Illustration: aufgerollte Pergamentrolle mit angesengten Rändern als Bildrahmen"></div>

    <div class="food-photo photo-dough" role="img" aria-label="Foto: Hände formen Maultaschen auf bemehlter Arbeitsfläche"></div>
    <div class="food-photo photo-knoedel" role="img" aria-label="Foto: aufgebrochene Knödel mit Soße und Schnittlauch"></div>
    <div class="food-photo photo-maultasche" role="img" aria-label="Foto: gebratene Maultasche mit Zwiebeln und Petersilie"></div>

    <footer class="visit-band">
      <p class="visit-call">Besuchen Sie uns an unserem Stand (Monza-Rot)<br>auf dem Brunnwaldener Wochenmarkt!</p>
      <p class="visit-tagline">Rinnfalten &amp; Co – Weil Qualität man schmeckt.</p>
    </footer>
  </main>
</body>
</html>
```